Clean bold and classy business card front and back
Rin can be the logo
My name Dorian Hesketh as owner
Phone email and address
Owner Dorian Hesketh
Phone 8505550147
Email ridgelineinsulate@mailbox.test
Address170 frank pais rd Havana fl 32390

Industry/Entity Type

Business

Contact Information for Business Card

Owner Dorian Hesketh
Phone 8505550147

Requirements
Must have
• Ridgeline insulate co under Rin logo
Nice to have
• Bold and clean. Maybe use Rin as logo and name under it. Have logo on one side and info on the other side with logo also
• Put a pic up. It doesn't have to be that but something that can be used
• Try some fancy fonts also

```html
<!DOCTYPE html>
<html lang="en">
<head>
<meta charset="utf-8">
<title>Ridgeline Insulate Co — Business Card</title>
<link rel="stylesheet" href="https://fonts.googleapis.com/css2?family=Anton&family=Arimo:wght@400;700&family=Oswald:wght@700&display=swap">
<style>
  :root{
    --brand-blue:#0556a4;
    --paper:#ffffff;
    --backdrop:#efebe4;
  }
  *{box-sizing:border-box;margin:0;padding:0}
  html,body{width:1189px;height:1200px;overflow:hidden}
  body{background:var(--backdrop);position:relative;font-family:"Arimo",Arial,sans-serif}
  .card{position:absolute;top:147px;width:482px;height:844px}
  .card--front{left:75px;background:var(--brand-blue)}
  .card--front svg{display:block}
  .card--back{left:631px;background:var(--paper);color:var(--brand-blue);text-align:center}
  .brand-mark{position:absolute;left:0;right:0;top:92px;display:flex;align-items:center;justify-content:center;gap:18px}
  .brand-mark__square{width:44px;height:44px;background:var(--brand-blue)}
  .brand-mark__name{font-family:"Anton",Impact,sans-serif;font-size:104px;line-height:1;font-weight:400}
  .brand-block{position:absolute;left:91px;top:222px;width:298px}
  .brand-block svg{display:block;overflow:visible}
  .owner-name{position:absolute;left:0;right:0;top:412px;font-family:"Oswald","Arial Narrow",sans-serif;font-weight:700;font-size:44px;line-height:1;letter-spacing:-0.5px}
  .owner-role{position:absolute;left:0;right:0;top:459px;font-size:31px;line-height:1}
  .phone{position:absolute;left:0;right:0;top:578px;font-size:42px;line-height:1}
  .email{position:absolute;left:0;right:0;top:634px;font-size:21.5px;line-height:1}
  .address-band{position:absolute;left:0;right:0;bottom:0;height:81px;background:var(--brand-blue);color:var(--paper);display:flex;align-items:center;justify-content:center;font-weight:700;font-size:22.5px;word-spacing:5px;letter-spacing:0.6px}
</style>
</head>
<body>
  <section class="card card--front" aria-label="Card front">
    <svg width="482" height="844" viewBox="0 0 482 844">
      <text transform="translate(253,730) rotate(-90)" x="0" y="0" textLength="620" lengthAdjust="spacingAndGlyphs" font-family="Anton, Impact, sans-serif" font-size="118" fill="#fff">RIDGELINE</text>
      <text transform="translate(318,730) rotate(-90)" x="0" y="0" textLength="620" lengthAdjust="spacing" font-family="Arimo, Arial, sans-serif" font-weight="700" font-size="66" fill="#fff">INSULATE CO</text>
    </svg>
  </section>

  <section class="card card--back" aria-label="Card back">
    <div class="brand-mark">
      <span class="brand-mark__square"></span>
      <span class="brand-mark__name">RIN</span>
    </div>
    <div class="brand-block">
      <svg width="298" height="80" viewBox="0 0 298 80">
        <text x="0" y="48" textLength="298" lengthAdjust="spacingAndGlyphs" font-family="Anton, Impact, sans-serif" font-size="54" fill="#0556a4">RIDGELINE</text>
        <text x="0" y="78" textLength="298" lengthAdjust="spacing" font-family="Arimo, Arial, sans-serif" font-weight="700" font-size="27" fill="#0556a4">INSULATE CO</text>
      </svg>
    </div>
    <p class="owner-name">Dorian Hesketh</p>
    <p class="owner-role">Owner</p>
    <p class="phone">8505550147</p>
    <p class="email">ridgelineinsulate@mailbox.test</p>
    <p class="address-band">482 tilden oak rd Havana fl 32390</p>
  </section>
</body>
</html>
```